Consulting/Brand Licensing business needs business card

We need a business card created for our IP company, that also does consulting and brand licensing. We would like this card to be vague, as our other business' are in the cannabis industry and this is a non-cannabis touching entity. Perhaps something that hints vaguely at the industry without alerting or possibly offending the receiver.

Target Market(s)

CEOs/Key Decision Makers/Industry Leaders

Contact Information for Business Card

No address, simply list Seattle, WA. Phone: 206-555-0143. Name: Dario Lindqvist // email: Dario@velmarcoast.com

Colors

Designer to choose colors to be used in the design.

Requirements
Must have
• Logo, Name, Email, Phone number, "Consulting, Licensing and Branding Specialists"
Nice to have
• We would like this to be more professional than playful.

```html
<!DOCTYPE html>
<html lang="en">
<head>
<meta charset="utf-8">
<title>Velmar Coast, Inc — Business Card</title>
<link rel="stylesheet" href="https://fonts.googleapis.com/css2?family=Bebas+Neue&family=Questrial&display=swap">
<style>
  :root {
    --backdrop: #2b2d31;
    --card-white: #ffffff;
    --card-black: #0b0b0c;
    --accent: #e2462a;
    --ink: #1c1c1c;
    --silver: #b9babd;
  }
  * { box-sizing: border-box; margin: 0; padding: 0; }
  html, body {
    width: 1200px;
    height: 900px;
    overflow: hidden;
    background: var(--backdrop);
  }
  .canvas {
    position: relative;
    width: 1200px;
    height: 900px;
  }
  .card {
    position: absolute;
    overflow: hidden;
    border-radius: 3px;
    box-shadow: 0 14px 30px rgba(0, 0, 0, 0.45);
  }

  /* Back */
  .card--back {
    left: 620px;
    top: 130px;
    width: 520px;
    height: 300px;
    background: var(--card-black);
    display: flex;
    flex-direction: column;
    align-items: center;
    justify-content: center;
    gap: 14px;
  }
  .brand {
    display: flex;
    align-items: center;
    gap: 12px;
  }
  .brand__square {
    display: block;
    flex: none;
  }
  .brand__name {
    font-family: "Bebas Neue", sans-serif;
    letter-spacing: 1px;
    line-height: 1;
    white-space: nowrap;
  }
  .card--back .brand__square {
    width: 34px;
    height: 34px;
    background: var(--silver);
  }
  .card--back .brand__name {
    color: var(--silver);
    font-size: 56px;
  }
  .tagline {
    font-family: "Questrial", sans-serif;
    font-size: 15px;
    letter-spacing: 0.5px;
    color: var(--silver);
  }

  /* Front */
  .card--front {
    left: 70px;
    top: 460px;
    width: 560px;
    height: 320px;
    background: var(--card-white);
  }
  .accent-band {
    position: absolute;
    left: 0;
    bottom: 0;
    width: 240px;
    height: 28px;
  }
  .card--front .brand {
    position: absolute;
    left: 44px;
    top: 42px;
  }
  .card--front .brand__square {
    width: 30px;
    height: 30px;
    background: var(--accent);
  }
  .card--front .brand__name {
    color: var(--accent);
    font-size: 48px;
  }
  .contact {
    position: absolute;
    left: 300px;
    top: 132px;
    font-family: "Questrial", sans-serif;
    font-size: 18px;
    line-height: 1.3;
    color: var(--ink);
  }
  .contact__name {
    font-family: "Bebas Neue", sans-serif;
    font-size: 32px;
    color: var(--accent);
    letter-spacing: 0.5px;
    line-height: 1.05;
  }
  .contact__phone { color: var(--accent); }
</style>
</head>
<body>
<main class="canvas">
  <section class="card card--back" aria-label="Card back">
    <div class="brand">
      <span class="brand__square" aria-hidden="true"></span>
      <p class="brand__name">Velmar Coast, Inc</p>
    </div>
    <p class="tagline">Consulting, Licensing and Branding Specialists</p>
  </section>

  <section class="card card--front" aria-label="Card front">
    <div class="brand">
      <span class="brand__square" aria-hidden="true"></span>
      <p class="brand__name">Velmar Coast, Inc</p>
    </div>
    <div class="contact">
      <p class="contact__name">Dario Lindqvist</p>
      <p class="contact__city">Seattle, WA</p>
      <p class="contact__phone">206.555.0143</p>
      <p class="contact__email">Dario@velmarcoast.com</p>
    </div>
    <svg class="accent-band" viewBox="0 0 240 28" aria-hidden="true">
      <polygon points="0,0 224,0 240,28 0,28" fill="var(--accent)"/>
    </svg>
  </section>
</main>
</body>
</html>
```